Hall of Fame annnouncement graphic for social media

I need a social media Hall of Fame announcement designed in the styles of some of the examples I've posted. I have attached the two gentlemens head shots ... the names are Dale Prosser and Jim Harnden

It is for the BRIARWOOD LINKS HONOR SOCIETY also include 2026 Inductees ... I have also attached the logo... make the post in similar colors as the logo.

I need this tomorrow so I am going to pick a winner in the next 24 hours.

```html
<!DOCTYPE html>
<html lang="en">
<head>
<meta charset="utf-8">
<title>Briarwood Links Honor Society – 2026 Inductees</title>
<link href="https://fonts.googleapis.com/css2?family=Roboto+Condensed:wght@700;800;900&display=swap" rel="stylesheet">
<style>
  :root{
    --page:#13266e;
    --paper:#f2f2f2;
    --band:#0f2c8f;
    --band-light:#1f47c4;
    --red:#a80c0c;
    --red-dark:#8e0a0a;
    --navy:#0e1f6b;
    --white:#ffffff;
  }
  *{margin:0;padding:0;box-sizing:border-box}
  html,body{width:1200px;height:847px;overflow:hidden}
  body{background:var(--page);font-family:"Roboto Condensed",Arial,sans-serif;position:relative}
  .post{position:absolute;left:120px;top:153px;width:960px;height:540px;background:var(--paper);overflow:hidden}
  .post svg.frame{position:absolute;inset:0}
  .backdrop-photo{position:absolute;left:245px;top:0;width:470px;height:540px;
    background:linear-gradient(180deg,rgba(160,160,160,.18),rgba(120,120,140,.25));}
  .blue-band{position:absolute;left:0;top:208px;width:960px;height:220px;background:var(--band)}
  .portrait{position:absolute;bottom:0;border-radius:140px 140px 0 0;
    background:linear-gradient(180deg,#9a9a9a 0%,#d9d9d9 45%,#f4f4f4 100%)}
  .portrait--left{left:0;width:327px;height:356px}
  .portrait--right{left:669px;width:291px;height:359px}
  .inductee{position:absolute;top:30px;width:168px;text-align:center;color:var(--white)}
  .inductee--left{left:67px}
  .inductee--right{left:726px}
  .inductee .rule{display:flex;align-items:center;gap:6px;justify-content:center}
  .inductee .rule i{display:block;height:2px;background:var(--white);flex:1}
  .inductee .stars{color:var(--navy);font-size:22px;letter-spacing:2px;font-style:normal;line-height:1}
  .inductee h2{font-weight:900;font-size:38px;line-height:36px;letter-spacing:-.5px;margin:6px 0 6px;text-transform:uppercase}
  .inductee .base{height:2px;background:var(--white)}
  .society-name{position:absolute;left:245px;width:470px;top:52px;text-align:center;color:var(--navy);
    font-weight:800;font-size:26px;line-height:30px;letter-spacing:1px;text-transform:uppercase}
  .headline{position:absolute;left:300px;width:360px;text-align:center;text-transform:uppercase}
  .headline--top{top:154px;color:var(--red);font-weight:900;font-size:44px;letter-spacing:-.5px}
  .headline--main{top:212px;color:var(--paper);font-weight:900;letter-spacing:-1px}
  .headline--main span{display:block}
  .headline--main .l1{font-size:96px;line-height:96px}
  .headline--main .l2{font-size:84px;line-height:100px}
  .class-bar{position:absolute;left:314px;top:444px;width:354px;height:52px;background:var(--red);
    display:flex;align-items:center;justify-content:center;gap:10px;color:var(--white)}
  .class-bar b{font-weight:900;font-size:30px}
  .class-bar i{font-style:normal;font-size:12px;letter-spacing:1px}
</style>
</head>
<body>
  <main class="post">
    <div class="backdrop-photo" role="img" aria-label="Faded black-and-white photo of a golfer mid-swing"></div>
    <div class="blue-band"></div>

    <svg class="frame" width="960" height="540" viewBox="0 0 960 540" aria-hidden="true">
      <polygon points="170,195 255,155 255,260" fill="var(--band-light)"/>
      <polygon points="46,0 255,0 255,155 46,245" fill="var(--red)"/>
      <polygon points="790,195 705,155 705,260" fill="var(--band-light)"/>
      <polygon points="705,0 912,0 912,245 705,155" fill="var(--red)"/>
    </svg>

    <div class="portrait portrait--left" role="img" aria-label="Black-and-white headshot of Jim Harnden in a white polo"></div>
    <div class="portrait portrait--right" role="img" aria-label="Black-and-white headshot of Dale Prosser in a white polo"></div>

    <div class="inductee inductee--left">
      <div class="rule"><i></i><em class="stars">★★★</em><i></i></div>
      <h2>Jim<br>Harnden</h2>
      <div class="base"></div>
    </div>
    <div class="inductee inductee--right">
      <div class="rule"><i></i><em class="stars">★★★</em><i></i></div>
      <h2>Dale<br>Prosser</h2>
      <div class="base"></div>
    </div>

    <div class="society-name">Briarwood Links<br>Honor Society</div>

    <h1 class="headline headline--top">Briarwood Links</h1>
    <div class="headline headline--main"><span class="l1">Honor</span><span class="l2">Society</span></div>

    <div class="class-bar"><i>★★★</i><b>2026 INDUCTEES</b><i>★★★</i></div>
  </main>
</body>
</html>
```